Business card design needed

Need a business card for a new Company in Melbourne called Brightway Lending Choices. This company is a Mortgage Brokering company that facilitates mainly Residential loans, but also Business and Commercial loans.
I would like something professional as I am in the finance industry.
I would like Brightway Lending font wise to be bigger than choices, with the word choices to sit below the Brightway Lending.

Industry/Entity Type

Finance

Contact Information for Business Card

Daniel Westhorpe | Lending Specialist
Brightway Lending Choices
P.O Box 517 Elmvale Vic.3071
T. +61 3 9000 4171 | F. +61 3 9000 6235| M. +61 400572904
www.brightwaylending.example

Daniel Westhorpe is a credit representative (CRN 572914)of KRVMO Pty.Ltd (Australian Credit Licence No 648502)

Requirements
Must have
• Daniel Westhorpe is a credit representative (CRN 572914)of KRVMO Pty.Ltd (Australian Credit Licence No 648502) has to sit at the bottom of the card, in the smallest readable font.

The logo to be designed is the most crucial thing for me.

```html
<!DOCTYPE html>
<html lang="en">
<head>
<meta charset="utf-8">
<title>Brightway Lending Choices – Business Card</title>
<link rel="stylesheet" href="https://fonts.googleapis.com/css2?family=Archivo+Black&family=Lato:wght@400;700&display=swap">
<style>
  :root {
    --backdrop: #8f9091;
    --card-dark: #2a2b2c;
    --card-light: #ffffff;
    --accent: #5ad2e8;
    --ink: #1f1f1f;
    --ink-soft: #444444;
    --ghost: #f1f1f1;
    --white: #ffffff;
  }
  * { margin: 0; padding: 0; box-sizing: border-box; }
  html, body {
    width: 1200px; height: 741px; overflow: hidden;
    background: var(--backdrop);
  }
  .stage {
    position: relative; width: 1200px; height: 741px;
    display: flex; align-items: center; justify-content: center; gap: 40px;
  }
  .card {
    position: relative; width: 520px; height: 318px; overflow: hidden;
    box-shadow: 0 8px 20px rgba(0,0,0,.25);
  }

  /* Front side */
  .card--front { background: var(--card-dark); }
  .front__rule {
    position: absolute; left: 0; right: 0; top: 146px; height: 6px;
    background: var(--accent);
  }
  .front__band {
    position: absolute; left: 0; right: 0; top: 176px; height: 30px;
    background: var(--accent);
  }
  .front__name {
    position: absolute; left: 0; right: 0; top: 96px;
    font-family: "Archivo Black", sans-serif; color: var(--white);
    text-align: center; text-transform: uppercase; line-height: 1;
  }
  .front__name-main { display: block; font-size: 38px; letter-spacing: 1px; }
  .front__name-sub { display: block; font-size: 20px; letter-spacing: 6px; margin-top: 34px; }

  /* Back side */
  .card--back { background: var(--card-light); }
  .back__ghost {
    position: absolute; left: 250px; top: 62px;
    font-family: "Archivo Black", sans-serif; color: var(--ghost);
    text-transform: uppercase; line-height: .95; font-size: 44px;
  }
  .back__ghost span { display: block; }
  .back__name {
    position: absolute; left: 24px; top: 22px;
    font-family: "Archivo Black", sans-serif; color: var(--ink);
    text-transform: uppercase; line-height: 1.05;
  }
  .back__name-main { display: block; font-size: 20px; }
  .back__name-sub { display: block; font-size: 13px; letter-spacing: 4px; }
  .holder {
    position: absolute; right: 0; top: 96px; width: 272px; height: 52px;
    background: var(--accent); padding: 0 16px;
    display: flex; align-items: center;
    font-family: "Lato", sans-serif; color: var(--white);
  }
  .holder__name {
    font-size: 19px; font-weight: 400; letter-spacing: .5px;
    text-transform: uppercase; color: var(--white);
  }
  .contact {
    position: absolute; left: 24px; bottom: 36px;
    font-family: "Lato", sans-serif; color: var(--ink);
    font-size: 11.5px; line-height: 1.32; list-style: none;
  }
  .disclaimer {
    position: absolute; left: 24px; right: 24px; bottom: 12px;
    font-family: "Lato", sans-serif; color: var(--ink-soft);
    font-size: 7px; line-height: 1.2; white-space: nowrap;
  }
</style>
</head>
<body>
<main class="stage">
  <section class="card card--front" aria-label="Card front">
    <div class="front__rule"></div>
    <div class="front__band"></div>
    <h1 class="front__name">
      <span class="front__name-main">Brightway Lending</span>
      <span class="front__name-sub">Choices</span>
    </h1>
  </section>

  <section class="card card--back" aria-label="Card back">
    <div class="back__ghost" aria-hidden="true">
      <span>Brightway</span><span>Lending</span><span>Choices</span>
    </div>
    <div class="back__name">
      <span class="back__name-main">Brightway Lending</span>
      <span class="back__name-sub">Choices</span>
    </div>
    <div class="holder">
      <h2 class="holder__name">Daniel Westhorpe</h2>
    </div>
    <ul class="contact">
      <li>T. +61 3 9000 4171</li>
      <li>F. +61 3 9000 6235</li>
      <li>M. +61 400572904</li>
      <li>Email: info@brightwaylending.example</li>
      <li>www.brightwaylending.example</li>
      <li>Lending Specialist Brightway Lending Choices</li>
      <li>P.O Box 517 Elmvale Vic.3071</li>
    </ul>
    <p class="disclaimer">Daniel Westhorpe is a credit representative (CRN 572914) of KRVMO Pty.Ltd (Australian Credit Licence No 648502)</p>
  </section>
</main>
</body>
</html>
```